E-Commerce Website Update for Bamboo Poles Company

Existing website at:

http://www.reedcraftstudio.example/
http://www.reedcraftstudio.example/pages/product-and-price-list

Two pages to design: home page and "price list" page.

Info for home page as follows:

HOME PAGE:

Header:
Company Name: reedcraft studio
Telephone: 1 888 412 5093

Across the top:
Home | Price List | Blog | FAQ | About | Contact

Down the side:
About Bamboo
Wedding Arbors
Bamboo For Flutes
Black Bamboo
Spotted Bamboo
Bamboo Carpentry
Photo Gallery
All Products & Prices
Blog
FAQ
About
Contact

Should have shopping cart and search buttons on top.
Please see ai file, attached for logo (leaf) and font
In addition the homepage should have one or two sections for promotions

Chosen design will be asked to help deign a PRODUCT AND PRICE LIST page similar to the one we have now, but with "LEARN MORE" and "ORDER NOW" buttons for each item.
Updates

Reason: Thanks  for all the designs so far; giving an extra week for extra consideration.

Target Market(s)

Consumers, wedding planners.

Industry/Entity Type

Shopping

Requirements
Must have
• Clean, easy to read design.
Should not have
• No flash animation.

```html
<!DOCTYPE html>
<html lang="en">
<head>
<meta charset="utf-8">
<title>reedcraft studio — Bamboo Poles</title>
<link href="https://fonts.googleapis.com/css2?family=Ubuntu:wght@300;400;500;700&family=Open+Sans:wght@400;600;700;800&family=Arimo:wght@400;700&display=swap" rel="stylesheet">
<style>
:root{
  --green:#6cbf3a;
  --green-dark:#4f9a25;
  --green-light:#8fd45a;
  --ink:#3c3c3c;
  --muted:#7a7a7a;
  --line:#dcdcdc;
  --page-bg:#efefef;
  --white:#ffffff;
  --panel:#9c9c9c;
  --dark-btn:#1d1d1d;
}
*{margin:0;padding:0;box-sizing:border-box}
html,body{width:1200px;height:905px;overflow:hidden;background:var(--page-bg)}
.page{position:relative;width:1400px;height:1056px;transform:scale(.857143);transform-origin:0 0;font-family:"Arimo",sans-serif;color:var(--ink);background:linear-gradient(#fff 0,#f3f3f3 60%,var(--page-bg) 100%)}
.backdrop{position:absolute;left:0;top:0;width:1400px;height:510px;background:radial-gradient(ellipse at 15% 40%,#8fe04a 0,#3aa114 35%,#1f6e0a 70%),linear-gradient(90deg,#2b8a10,#6fd130 30%,#2f9a12 50%,#76d238 80%,#2b8a10);background-blend-mode:soft-light}
.shell{position:absolute;left:220px;top:48px;width:960px;height:470px;background:var(--white);border-radius:4px 4px 0 0}
.brand{position:absolute;left:20px;top:28px;display:flex;align-items:center;gap:10px;font-family:"Open Sans",sans-serif;font-weight:600;font-size:32px;color:var(--ink);letter-spacing:-.5px}
.brand-dot{width:14px;height:14px;border-radius:50%;background:var(--green)}
.top-links{position:absolute;right:12px;top:27px;display:flex;font-family:"Arimo",sans-serif;font-size:11px;color:#777}
.top-links a{color:#777;text-decoration:none;padding:0 16px;border-left:1px solid #ccc;line-height:12px}
.top-links a:first-child{border-left:0}
.top-links a:last-child{padding-right:0}
.phone{position:absolute;left:255px;top:74px;font-family:"Open Sans",sans-serif;font-size:16px;font-weight:700;color:#555}
.phone span{font-weight:400;color:#999;margin-left:4px}
.search-tray{position:absolute;left:470px;top:62px;width:490px;height:42px;background:linear-gradient(#fbfbfb,#ececec);border-radius:14px 0 0 0;border-top:1px solid #e3e3e3;border-left:1px solid #e3e3e3}
.search{position:absolute;left:12px;top:8px;width:236px;height:28px;border-radius:14px;background:#fff;border:1px solid #d6d6d6;display:flex;align-items:center;padding-left:10px;font-size:11px;color:#888}
.search svg{margin-right:10px}
.go{position:absolute;right:3px;top:3px;width:32px;height:20px;border-radius:10px;background:linear-gradient(var(--green-light),var(--green-dark));color:#fff;font-family:"Ubuntu",sans-serif;font-weight:700;font-size:12px;text-align:center;line-height:20px}
.cart{position:absolute;left:266px;top:4px;display:flex;align-items:center;gap:6px;font-size:11px;color:#999}
.cart b{color:#555;font-family:"Open Sans",sans-serif;font-weight:700}
.nav{position:absolute;left:0;top:104px;width:960px;height:46px;background:linear-gradient(#7fcb45,#62b62c);display:flex;align-items:center;padding-left:10px}
.nav a{font-family:"Open Sans",sans-serif;font-size:10.5px;font-weight:600;color:#fff;text-decoration:none;padding:0 8px;border-left:1px solid rgba(255,255,255,.45);line-height:12px;letter-spacing:-.2px}
.nav a.current{background:linear-gradient(#555,#1c1c1c);border-radius:4px;padding:10px 9px;border-left:0;margin-right:0;box-shadow:0 2px 2px rgba(0,0,0,.3)}
.nav a.current + a{border-left:0}
.hero{position:absolute;left:230px;top:212px;width:941px;height:297px;border-radius:4px;background:radial-gradient(ellipse at 12% 25%,#bdbdbd 0,#a8a8a8 40%,#979797 100%)}
.hero h1{position:absolute;left:17px;top:28px;font-family:"Open Sans",sans-serif;font-weight:800;font-size:21px;color:#fff;letter-spacing:-.2px;width:555px;padding-bottom:12px;border-bottom:1px solid rgba(255,255,255,.35)}
.hero .lead{position:absolute;left:18px;top:86px;font-size:11px;font-weight:700;color:#e7ffc9}
.hero .copy{position:absolute;left:18px;top:112px;width:505px;font-size:10.5px;line-height:22px;color:#fff}
.hero .copy strong{display:block;font-size:11px}
.read-more{position:absolute;left:14px;top:237px;width:155px;height:43px;border-radius:4px;background:linear-gradient(#fdfdfd,#dcdcdc);box-shadow:0 2px 3px rgba(0,0,0,.25);font-family:"Open Sans",sans-serif;font-weight:800;font-size:21px;color:#6a6a6a;text-align:center;line-height:43px}
.hero-photo{position:absolute;left:628px;top:10px;width:302px;height:275px;border:2px solid #cfcfcf;background:linear-gradient(#9fb7d6 0,#d9e1ea 35%,#b69062 60%,#7a5a3b 100%)}
.tabs{position:absolute;left:231px;top:549px;display:flex;gap:10px}
.tab{height:29px;padding:0 9px;font-family:"Ubuntu",sans-serif;font-weight:300;font-size:17px;line-height:29px;color:#fff;background:#a9a9a9;border-radius:2px}
.tab.active{background:var(--green);font-weight:400;position:relative}
.tab.active::after{content:"";position:absolute;left:10px;bottom:-6px;border:6px solid transparent;border-bottom:0;border-top-color:var(--green)}
.card{position:absolute;top:600px;width:217px;height:300px;background:#fff;border:1px solid #e0e0e0;border-radius:3px 3px 0 0;box-shadow:0 0 6px rgba(0,0,0,.06)}
.card h2{position:absolute;left:15px;top:20px;font-family:"Open Sans",sans-serif;font-weight:700;font-size:14.5px;color:#444}
.card .thumb{position:absolute;left:9px;top:56px;width:199px;height:138px;border:1px solid #dedede;background:linear-gradient(#fff,#f1f1f1)}
.thumb .swatch{position:absolute;left:50%;top:10px;transform:translateX(-50%);width:80px;height:116px;background:linear-gradient(90deg,#4b8a2a,#9ccc5d,#4b8a2a)}
.thumb .swatch.tan{background:linear-gradient(90deg,#c59a55,#f0d59a,#c59a55);width:96px}
.card .price-row{position:absolute;left:9px;top:202px;width:199px;height:30px;border-top:1px solid #e2e2e2;border-bottom:1px solid #e2e2e2}
.price{position:absolute;left:2px;top:4px;font-size:19px;color:#7c7c7c}
.learn{position:absolute;right:0;top:4px;width:85px;height:21px;border-radius:2px;background:#b3b3b3;color:#fff;font-size:11px;font-weight:700;line-height:21px;text-align:center}
.card p{position:absolute;left:10px;top:245px;width:197px;text-align:center;font-size:10px;line-height:13px;color:#666}
.card-foot{position:absolute;top:895px;width:237px;height:30px}
.order{position:absolute;top:904px;width:106px;height:30px;border-radius:3px;background:linear-gradient(#3a3a3a,var(--dark-btn));color:#fff;font-family:"Open Sans",sans-serif;font-weight:700;font-size:13.5px;line-height:30px;text-align:center;box-shadow:0 2px 3px rgba(0,0,0,.35)}
.order.featured{background:linear-gradient(var(--green-light),var(--green-dark))}
.footer-line{position:absolute;left:230px;top:966px;width:942px;border-top:1px solid #d4d4d4}
.copyright{position:absolute;left:231px;top:988px;font-size:11px;color:#888}
</style>
</head>
<body>
<div class="page">
  <div class="backdrop" role="img" aria-label="Close-up photograph of green bamboo stalks"></div>

  <header class="shell">
    <div class="brand"><span>reedcraft studio</span><span class="brand-dot"></span></div>
    <nav class="top-links">
      <a href="#">Home</a><a href="#">Price List</a><a href="#">Blog</a><a href="#">FAQ</a><a href="#">About</a><a href="#">Contact</a>
    </nav>
    <div class="phone">TELEPHONE:<span>1 888 412 5093</span></div>
    <div class="search-tray">
      <div class="search">
        <svg width="10" height="10" viewBox="0 0 10 10"><circle cx="4" cy="4" r="3" fill="none" stroke="#666" stroke-width="1.5"/><line x1="6.3" y1="6.3" x2="9.3" y2="9.3" stroke="#666" stroke-width="1.5"/></svg>
        Type your Search here!
        <span class="go">Go</span>
      </div>
      <div class="cart">
        <svg width="48" height="44" viewBox="0 0 48 44"><line x1="26" y1="14" x2="40" y2="2" stroke="#555" stroke-width="2"/><path d="M3 14h42l-5 28H8z" fill="#7cc63f"/><path d="M3 14h42v5H3z" fill="#5fae26"/><g stroke="#bfe69a" stroke-width="1.5"><line x1="13" y1="22" x2="13" y2="38"/><line x1="20" y1="22" x2="20" y2="38"/><line x1="27" y1="22" x2="27" y2="38"/><line x1="34" y1="22" x2="34" y2="38"/></g></svg>
        <span><b>SHOPPING CART:</b> (03) items</span>
      </div>
    </div>
    <nav class="nav">
      <a class="current" href="#">ABOUT BAMBOO</a>
      <a href="#">WEDDING ARBORS</a>
      <a href="#">BAMBO FOR FLUTES</a>
      <a href="#">BLACK BAMBO</a>
      <a href="#">SPOTTED BAMBO</a>
      <a href="#">BAMBO CARPENTARY</a>
      <a href="#">PHOTO GALLERY</a>
      <a href="#">ALL PRODUCTS AND PRICES</a>
      <a href="#">CONTACT US</a>
    </nav>
  </header>

  <section class="hero">
    <h1>WELCOME TO YOUR POLE PROVIDER 1 888 412 5093</h1>
    <div class="lead">Bamboo poles at wholesale prices direct from Reedcraft Studio.</div>
    <div class="copy">
      <strong>Need bamboo poles at a competitive price? Welcome to your one-stop pole shop.</strong>
      We warehouse a variety of types poles in a variety of diameters, from 5/8" to 5 1/2", in lengths up to 8'. We have natural poles, moso (mao) timber poles, black poles spotted poles... and regular bamboo poles. Whatever your project may be, from flutes to weddings to roasting a pig, we have the perfect pole for you.
    </div>
    <div class="read-more">READ MORE</div>
    <div class="hero-photo" role="img" aria-label="Photograph of tall stacks of bamboo poles leaning together outdoors"></div>
  </section>

  <div class="tabs">
    <div class="tab active">New Products</div>
    <div class="tab">Featured Procuts</div>
    <div class="tab">Best Selling Products</div>
  </div>

  <article class="card" style="left:230px">
    <h2>MAO BAMBOO POLES -...</h2>
    <div class="thumb"><div class="swatch" style="width:20px" role="img" aria-label="Product photo of a bamboo stalk with stones and a flower"></div></div>
    <div class="price-row"><span class="price">$95.99</span><span class="learn">Learn more ›</span></div>
    <p>Shop this wide selection of Kelso steel mixing bowls, which are sure to put a smile on any cook's face.</p>
  </article>
  <article class="card" style="left:468px">
    <h2>NAN BAMBOO POLES</h2>
    <div class="thumb"><div class="swatch tan" role="img" aria-label="Product photo of a bamboo mirror frame"></div></div>
    <div class="price-row"><span class="price">$95.99</span><span class="learn">Learn more ›</span></div>
    <p>Shop this wide selection of Kelso steel mixing bowls, which are sure to put a smile on any cook's face.</p>
  </article>
  <article class="card" style="left:706px">
    <h2>MAO BAMBOO POLES -...</h2>
    <div class="thumb"><div class="swatch" style="width:112px" role="img" aria-label="Product photo of a green bamboo square frame"></div></div>
    <div class="price-row"><span class="price">$95.99</span><span class="learn">Learn more ›</span></div>
    <p>Shop this wide selection of Kelso steel mixing bowls, which are sure to put a smile on any cook's face.</p>
  </article>
  <article class="card" style="left:944px">
    <h2>NAN BAMBOO POLES</h2>
    <div class="thumb"><div class="swatch" style="width:64px;height:126px" role="img" aria-label="Product photo of three green bamboo poles"></div></div>
    <div class="price-row"><span class="price">$95.99</span><span class="learn">Learn more ›</span></div>
    <p>Shop this wide selection of Kelso steel mixing bowls, which are sure to put a smile on any cook's face.</p>
  </article>

  <div class="order" style="left:285px">ORDER NOW</div>
  <div class="order featured" style="left:523px">ORDER NOW</div>
  <div class="order" style="left:761px">ORDER NOW</div>
  <div class="order" style="left:999px">ORDER NOW</div>

  <footer>
    <div class="footer-line"></div>
    <div class="copyright">Copyright © 2011 Reedcraft Studio. All Rights Reserved. All prices USD.</div>
  </footer>
</div>
</body>
</html>
```